SEO and image area for top of invitation website

We need to add an area on our final category pages for SEO text. Instead of just adding text, we'd like to develop a graphical approach that keeps with our soft, feminine look.

You can view an example of our current final category page at http://www.cardmeadow.example/invitations/boy-birthday

I've attached an image of what we're thinking it could look like, but you're welcome to alter the design.

The area should be the same width as our site, but can be any height you determine appropriate.

The winner of this project may be approached to develop the additional designs and backgrounds for us as another project. We additionally have several other projects we're interested in doing with the winner.
Updates

We have had a question about the right side of the banner, and what "Free Unlimited Proofs" mean.

About Free Unlimited Proofs:

We are a custom invitation printing company. When a customer orders an invitation from us, they tell us what information we want on the invitation. We then create an electronic sample, or "proof", of what it will look like. We then email it to the customer and they can tell us if they want to make any more changes. We will continue to send them samples, or what we call "proofs", until they are completely satisfied with the way it looks.

We offer Free UNLIMITED Proofs. Compared to our competitors, we are the only one to offer free unlimited proofs.

So, for the right side of this banner, we need an image, or a badge, promoting that we offer free unlimited proofs, and you can include that we are the only ones to do it, if your design has space for that information.

Also, keep in mind, that for other category pages, we may create different images or badges to put in this area - such as for our Low Price Guarantee or to promote a coupon or specific product, for example. So, your design should be able to work with various images on the right side.

Target Market(s)

Our demographic is 100% women, ages 25-60.

Industry/Entity Type

Seo

Requirements
Must have
• The area must have 3 things:
1) Area for the title of the page.
2) Area for SEO text describing the category page.
3) Area for an image. Keep in mind that this image may change for each category page. For this project, you will create an image for our offering of "Free Unlimited Proofs". On other pages, we may display other images we create such as "Low Price Guarantee" or images of certain products we'd like to promote. Just keep this in mind when you're making the design flow.
Nice to have
• Optional: Light design background. We wouldn't mind there being a slight graphical background to this area, to keep it interesting to the eye. Then, for other category pages, we may make additional backgrounds to use in this box area.

```html
<!DOCTYPE html>
<html lang="en">
<head>
<meta charset="utf-8">
<title>Boy Birthday Cards</title>
<link rel="stylesheet" href="https://fonts.googleapis.com/css2?family=Arvo&family=Cinzel:wght@700&display=swap">
<style>
:root{
  --page:#ffffff;
  --panel:#dcdcdc;
  --pattern:#d2d2d2;
  --frame:#f7f7f7;
  --mauve:#7a6970;
  --mauve-dark:#6b5b62;
  --sun:#f8cf4e;
  --sun-text:#f6c94a;
  --white:#ffffff;
}
*{margin:0;padding:0;box-sizing:border-box}
html,body{width:1200px;height:245px;overflow:hidden;background:var(--page)}
.banner{position:relative;width:1200px;height:245px}
.panel{
  position:absolute;left:47px;top:12px;width:1126px;height:224px;
  border-radius:16px;border:3px solid var(--frame);
  background:radial-gradient(circle at 50% 50%,var(--panel),var(--pattern));
  box-shadow:0 0 3px rgba(0,0,0,.35);
  overflow:hidden;
}
.title-tab{
  position:absolute;left:0;top:0;width:418px;height:60px;
  background:var(--mauve);border-radius:13px 0 9px 0;
  display:flex;align-items:center;padding-left:20px;
}
.title-tab h1{
  font-family:'Arvo',serif;font-weight:400;font-size:33px;color:var(--sun-text);
  letter-spacing:.3px;
}
.seo-text{
  position:absolute;left:12px;top:75px;width:812px;height:128px;
  background:var(--mauve);border-radius:9px;
  box-shadow:0 0 4px rgba(0,0,0,.3);
  padding:12px 14px;
}
.seo-text p{
  font-family:'Cinzel',serif;font-weight:700;font-size:15.3px;line-height:26px;
  color:var(--white);letter-spacing:.3px;
}
.promo{
  position:absolute;left:850px;top:5px;width:240px;height:198px;
  box-shadow:0 0 4px rgba(0,0,0,.3);
}
.promo-head{
  height:92px;background:var(--sun);
  display:flex;align-items:center;justify-content:center;text-align:center;
  font-family:'Cinzel',serif;font-weight:700;font-size:22px;line-height:30px;color:var(--mauve-dark);
}
.promo-body{
  height:106px;background:var(--mauve);padding:9px 14px 0;text-align:center;
  font-family:'Cinzel',serif;font-weight:700;font-size:11.6px;line-height:15px;color:var(--white);
}
.brand-dot{position:absolute;left:1098px;top:186px}
</style>
</head>
<body>
<div class="banner">
  <section class="panel" role="img" aria-label="Light grey background with a faint repeating duck pattern">
    <div class="title-tab"><h1>Boy Birthday Cards</h1></div>
    <div class="seo-text">
      <p>Lorem ipsum dolor sit amet, consectetur adipiscing elit. Mauris sed tortor mauris, et mollis est. Curabitur lobortis neque ut ante venenatis mattis. Nullam nisl erat, suscipit eget viverra in, vestibulum eu mi. Integer elementum arcu magna, id porta odio.</p>
    </div>
    <aside class="promo">
      <div class="promo-head">Free, Unlimited<br>&amp; Exclusive!</div>
      <div class="promo-body">We offer FREE unlimited proofs, making sure each and every card is just right! Something you won't get anywhere else.</div>
    </aside>
  </section>
  <svg class="brand-dot" width="48" height="48" viewBox="0 0 48 48" role="img" aria-label="Brand mark">
    <circle cx="24" cy="24" r="22" fill="var(--white)" stroke="var(--mauve)" stroke-width="2"/>
  </svg>
</div>
</body>
</html>
```